Modern and Luxury Cosmetics Re-Brand

Looking for a professional, modern, and minimal packaging design to replace current look. Must serve to appeal to both old and young customers.

Our products have 22+ sea and earth minerals, 12 of which are unique to only one location. Think about thousands of mineral particles actively antioxidizing the skin, rejuvenating and renewing it as it is exposed.

Target Market(s)

Cosmetics, Beauty Products

Industry/Entity Type

Cosmetic

Colors

Designer to choose colors to be used in the design.

Requirements
Must have
• Elegant and Unique look. Minimal and appealing.

```html
<!DOCTYPE html>
<html lang="en">
<head>
<meta charset="utf-8">
<title>Nuvara Lightening Anti-Odor Cream Label</title>
<link rel="stylesheet" href="https://fonts.googleapis.com/css2?family=Cabin:wght@400;500;700&family=Open+Sans:wght@600;700&family=Roboto+Condensed:wght@700&display=swap">
<style>
  :root {
    --paper: #ffffff;
    --backdrop: #eeeff0;
    --teal: #3d8c94;
    --teal-deep: #236a70;
    --teal-mid: #4f9ea4;
    --teal-mist: #cfe3e4;
    --gold: #c9a450;
    --amber: #e9b640;
    --ink-white: #ffffff;
  }
  * { box-sizing: border-box; margin: 0; padding: 0; }
  html, body {
    width: 1200px;
    height: 2341px;
    overflow: hidden;
    background: var(--backdrop);
  }
  .label {
    position: relative;
    width: 1200px;
    height: 2341px;
    background: var(--paper);
    overflow: hidden;
    font-family: "Cabin", sans-serif;
  }
  .label-wave {
    position: absolute;
    left: 0; right: 0; bottom: 0;
    height: 1260px;
    background:
      radial-gradient(ellipse 90% 60% at 80% 85%, rgba(35,106,112,0.55), transparent 70%),
      linear-gradient(180deg, rgba(255,255,255,0) 0%, var(--teal-mist) 22%, var(--teal-mid) 58%, var(--teal-deep) 100%);
  }
  .top-band {
    position: absolute;
    top: 40px; left: 50%;
    transform: translateX(-50%);
    width: 640px; height: 56px;
    background: var(--teal);
  }
  .brand {
    position: absolute;
    top: 330px; left: 0; right: 0;
    display: flex; align-items: center; justify-content: center; gap: 34px;
  }
  .brand-dot {
    width: 58px; height: 58px;
    border-radius: 50%;
    background: var(--teal);
  }
  .brand-name {
    font-family: "Cabin", sans-serif;
    font-weight: 500;
    font-size: 190px;
    line-height: 1;
    color: var(--gold);
    letter-spacing: 2px;
  }
  .product-title {
    position: absolute;
    top: 820px; left: 0; right: 0;
    text-align: center;
    font-family: "Cabin", sans-serif;
    font-weight: 400;
    font-size: 104px;
    line-height: 1.12;
    letter-spacing: 2px;
    color: var(--teal);
  }
  .ingredient {
    position: absolute;
    top: 1240px; left: 0; right: 0;
    display: flex; align-items: center; justify-content: center; gap: 22px;
  }
  .made-with {
    background: var(--amber);
    color: var(--ink-white);
    font-family: "Open Sans", sans-serif;
    font-weight: 700;
    font-size: 46px;
    padding: 6px 26px;
    border-radius: 10px;
  }
  .sea-salts {
    font-family: "Open Sans", sans-serif;
    font-weight: 700;
    font-size: 84px;
    color: var(--teal);
    letter-spacing: 1px;
  }
  .minerals {
    position: absolute;
    top: 1360px; left: 50%;
    transform: translateX(-50%);
    width: 900px; height: 110px;
  }
  .minerals svg { position: absolute; inset: 0; }
  .minerals-text {
    position: absolute;
    top: 30px; left: 0; right: 0;
    text-align: center;
    font-family: "Open Sans", sans-serif;
    font-weight: 700;
    font-size: 54px;
    color: var(--ink-white);
    letter-spacing: 1px;
  }
  .claim {
    position: absolute;
    top: 1590px; left: 0; right: 0;
    text-align: center;
    font-family: "Open Sans", sans-serif;
    font-weight: 700;
    font-size: 68px;
    line-height: 1.2;
    color: var(--ink-white);
  }
  .usage {
    position: absolute;
    top: 1800px; left: 0; right: 0;
    text-align: center;
    font-family: "Open Sans", sans-serif;
    font-weight: 600;
    color: var(--ink-white);
  }
  .usage-lead { font-size: 32px; }
  .usage-areas { font-size: 44px; line-height: 1.22; }
  .volume {
    position: absolute;
    top: 2190px; left: 0; right: 0;
    text-align: center;
    font-family: "Roboto Condensed", sans-serif;
    font-weight: 700;
    font-size: 72px;
    color: var(--ink-white);
  }
</style>
</head>
<body>
  <main class="label">
    <div class="label-wave" role="img" aria-label="Soft teal wave with a field of mineral bubbles"></div>
    <div class="top-band"></div>

    <div class="brand">
      <span class="brand-dot"></span>
      <span class="brand-name">Nuvara</span>
    </div>

    <h1 class="product-title">LIGHTENING<br>ANTI-ODOR<br>CREAM</h1>

    <div class="ingredient">
      <span class="made-with">Made with</span>
      <span class="sea-salts">SEA SALTS</span>
    </div>

    <div class="minerals">
      <svg viewBox="0 0 900 110" width="900" height="110" aria-hidden="true">
        <line x1="0" y1="12" x2="870" y2="12" stroke="var(--teal)" stroke-width="4"/>
        <circle cx="880" cy="12" r="9" fill="none" stroke="var(--teal)" stroke-width="4"/>
        <path d="M40 12 H800 L770 100 H70 Z" fill="var(--teal)"/>
      </svg>
      <div class="minerals-text">MINERALS CREAM</div>
    </div>

    <p class="claim">Deodorant, stimulates<br>the respriatory tissue</p>

    <div class="usage">
      <p class="usage-lead">Used for</p>
      <p class="usage-areas">Under Arms, Sensitive Areas<br>&amp; Inner Thighs</p>
    </div>

    <p class="volume">300ml &#8494; 3.38 oz</p>
  </main>
</body>
</html>
```